依頼詳細
今ある幸せをメッセージとして書き、ご報告と共にお祈り頂きます。それ以外にも献歌などのサブ的なイベントのご案内を盛り込みたいと思います。
記載項目
詳細は添付資料をご確認願います。また、添付画像をご利用下さい。
サイズ
A4
ページ数
片面
希望イメージ
シンプル 複雑
単色 カラフル
暗い 明るい
日常 高級
遊び心 厳粛
未来的 伝統的
女性的 男性的
希望する色
納品ファイル
• イラストレーター形式 (.ai)
補足説明
アウトラインの有るもの、無いもの双方でお願い致します。添付画像は加工OKです。
■ 選んだ理由

選定にあたりましては弊社内でメイン画像枠の取り方(グラデーション/エッジ)で大きく選考しました。その結果、グラデーションが良いとの意見が過半数を超え、その中で更に投票方式によりhasuventoさんのご提案を選ばせて頂きました。慰霊そしてお客様へのメッセージが重要でありながら、サブイベントでは楽しさを感じさせ、行ってみたくなる。弊社が考えるコンセプトそのものでした。
また、度重なる修正依頼にも応じて頂けました事、本当に助かりました。

■ 提案者全員のお礼・コメント

皆様より本当に多くのご提案を頂きました事、この場をお借りし、御礼申し上げます。今回初めてポルメットへの依頼であり、ご提案頂けるのか不安がありましたが、ご応募頂いた皆様が当社のコンセプトをご理解・ご提案頂きました事また、その表現力、感謝の言葉しかありません。今後もお力を頂く機会があろうかと思いますし、是非、依頼をしたいと思います。その時にまたご提案頂く事が出来れば幸いです。

```html
<!DOCTYPE html>
<html lang="ja">
<head>
<meta charset="utf-8">
<title>キャンドル慰霊祭 開催の御案内</title>
<link rel="stylesheet" href="https://fonts.googleapis.com/css2?family=Noto+Serif+JP:wght@400;600;700&family=Noto+Sans+JP:wght@400;500;700&family=Great+Vibes&display=swap">
<style>
:root{
  --cream:#f6f0dc;
  --cream-deep:#ece2c4;
  --olive:#4d5a2c;
  --olive-dark:#3a4520;
  --moss:#6b7a3a;
  --ink:#3b3a2f;
  --gold:#b89a4e;
  --night:#15140f;
  --white:#ffffff;
}
*{box-sizing:border-box;margin:0;padding:0}
html,body{width:854px;height:1200px;overflow:hidden;background:var(--cream)}
.flyer{position:relative;width:854px;height:1200px;background:var(--cream);color:var(--ink);font-family:"Noto Serif JP",serif}
.brand{position:absolute;top:14px;left:0;width:100%;text-align:center;color:var(--olive)}
.brand-mark{display:inline-block;width:14px;height:14px;border-radius:50%;background:var(--gold);vertical-align:middle;margin-right:8px}
.brand-name{font-family:"Noto Serif JP",serif;font-size:24px;font-weight:600;letter-spacing:4px;vertical-align:middle}
.brand-sub{display:block;font-size:11px;letter-spacing:3px;margin-top:2px}
.title{position:absolute;top:78px;width:100%;text-align:center;font-size:60px;font-weight:700;color:var(--olive);letter-spacing:6px}
.subtitle-band{position:absolute;top:168px;left:100px;width:654px;height:40px;background:var(--olive);color:var(--white);text-align:center;font-size:24px;line-height:40px;letter-spacing:8px;font-weight:600}
.hero{position:absolute;top:212px;left:0;width:854px;height:380px;background:radial-gradient(ellipse at 35% 70%,#6f6a2e 0%,#2a2a16 35%,var(--night) 70%)}
.hero-fade{position:absolute;left:0;bottom:0;width:100%;height:70px;background:linear-gradient(to bottom,rgba(246,240,220,0),var(--cream))}
.hero-fade.top{top:0;bottom:auto;height:30px;background:linear-gradient(to top,rgba(246,240,220,0),var(--cream))}
.hero-message{position:absolute;top:236px;right:44px;height:320px;writing-mode:vertical-rl;white-space:nowrap;color:var(--white);font-size:16px;line-height:29px;letter-spacing:1px}
.date{position:absolute;top:596px;width:100%;text-align:center;font-size:22px;color:var(--olive-dark);font-weight:600}
.date small{font-size:16px;margin-left:14px}
.free-badge{position:absolute;top:632px;left:372px;width:110px;height:30px;background:var(--moss);color:var(--white);text-align:center;font-size:16px;line-height:30px;letter-spacing:4px}
.rule{position:absolute;top:676px;left:40px;width:774px;height:1px;background:var(--gold)}
.performer-photo{position:absolute;top:690px;left:50px;width:270px;height:205px;background:linear-gradient(135deg,#f3eee2,#d9cfb6)}
.event{position:absolute;top:690px;left:338px;width:480px}
.event-head{display:flex;align-items:baseline;gap:12px;color:var(--olive)}
.event-head .script{font-family:"Great Vibes",cursive;font-size:30px;color:var(--gold)}
.event-head .label{background:var(--olive);color:var(--white);font-size:16px;padding:2px 10px}
.event-head .time{font-size:14px}
.event-tag{font-family:"Great Vibes",cursive;color:var(--gold);font-size:22px;margin-top:6px}
.performer{font-size:20px;font-weight:700;color:var(--olive-dark)}
.performer span{font-size:14px;font-weight:400}
.event-text{font-family:"Noto Sans JP",sans-serif;font-size:12px;line-height:20px;margin-top:4px;width:220px}
.card-area{position:absolute;top:780px;left:575px;width:250px;height:190px;background:linear-gradient(160deg,#fbf8ee,#e9dfc2);border:1px solid var(--cream-deep)}
.side-box{position:absolute;left:20px;width:300px;height:120px;background:var(--olive);color:var(--white);font-family:"Noto Sans JP",sans-serif;font-size:11px;line-height:17px;padding:12px 150px 10px 12px}
.side-box.one{top:905px}
.side-box.two{top:905px;left:330px;width:235px;padding-right:118px;background:var(--moss)}
.side-photo{position:absolute;top:915px;width:130px;height:100px}
.side-photo.plush{left:180px;background:radial-gradient(circle,#fbfaf5,#d8d4c8)}
.side-photo.flowers{left:455px;width:100px;background:radial-gradient(circle,#e8b7b2,#c3a27a)}
.card-note{position:absolute;top:985px;left:580px;width:240px;font-family:"Noto Sans JP",sans-serif;font-size:11px;line-height:17px}
.notice{position:absolute;top:1044px;width:100%;text-align:center;font-family:"Noto Sans JP",sans-serif;font-size:12px}
.footer{position:absolute;top:1072px;left:0;width:854px;height:128px;background:var(--cream-deep);border-top:3px solid var(--olive)}
.footer-brand{position:absolute;top:26px;left:40px;color:var(--olive)}
.footer-brand .name{font-size:22px;font-weight:700;vertical-align:middle}
.footer-brand .brand-mark{width:22px;height:22px}
.footer-info{position:absolute;top:68px;left:72px;font-family:"Noto Sans JP",sans-serif;font-size:13px}
.footer-info b{font-size:18px;margin-left:16px;color:var(--olive-dark)}
.footer-tag{position:absolute;top:40px;right:40px;border:1px solid var(--olive);padding:6px 14px;font-size:12px;color:var(--olive)}
</style>
</head>
<body>
<main class="flyer">
  <header class="brand">
    <span class="brand-mark"></span><span class="brand-name">MIDORIE</span>
    <span class="brand-sub">Ceremony Hotel</span>
  </header>
  <h1 class="title">キャンドル慰霊祭</h1>
  <div class="subtitle-band">開催の御案内</div>

  <section class="hero" role="img" aria-label="暗がりに灯る多くのキャンドルと花の祭壇">
    <div class="hero-fade top"></div>
    <div class="hero-fade"></div>
  </section>
  <p class="hero-message">ただいた多くの願い<br>それは残された家族が日々の生活を<br>幸せにおくることではないでしょうか<br>大切な方への想いを込めて<br>今日のこと<br>これからのこと<br>家族みんなの笑顔とともに<br>メッセージとしてお届けいただき<br>たいと思います</p>

  <p class="date">2016年7月16日(土)<small>時間14:00〜18:00</small></p>
  <div class="free-badge">入場無料</div>
  <div class="rule"></div>

  <div class="performer-photo" role="img" aria-label="ギターを弾く歌手の写真"></div>
  <section class="event">
    <div class="event-head"><span class="script">Welcome</span><span class="label">献歌</span><span class="time">演奏時間 14:00〜 16:00〜</span></div>
    <p class="event-tag">Live</p>
    <p class="performer">青木 沙耶 <span>さん</span></p>
    <p class="event-text">地元を中心に活動するシンガーソングライター。透明感のあるナチュラルな歌声で、ジャンルを問わず幅広い楽曲を届けています。心に寄り添う歌をお楽しみください。</p>
  </section>

  <div class="card-area" role="img" aria-label="リボンの付いたメッセージカード"></div>

  <div class="side-box one">ぬいぐるみの中に想いを詰めて、ご家族の記念にお作りいただけます。</div>
  <div class="side-photo plush" role="img" aria-label="白いくまのぬいぐるみ"></div>
  <div class="side-box two">プリザーブドフラワーのお持ち帰りもご用意しております。</div>
  <div class="side-photo flowers" role="img" aria-label="小さな花のアレンジメント"></div>

  <p class="card-note">受付時にご案内のお手紙を差し上げます。お手紙にご記入いただき祭壇へお供えください。</p>
  <p class="notice">すべて入場無料となっております。ご家族・ご友人お誘いあわせの上ご来場ください。</p>

  <footer class="footer">
    <div class="footer-brand"><span class="brand-mark"></span><span class="name">セレモニーホテルミドリエ</span></div>
    <p class="footer-info">緑ヶ丘市花町1丁目2番3号<b>TEL.0120-000-481</b></p>
    <div class="footer-tag">2016キャンドル慰霊祭 多目的</div>
  </footer>
</main>
</body>
</html>
```